Provide bookkeeping and accounting services to small and growing businesses

We need website and logo design using the name Daltonby as the logo.
The target audience are small companies and startups who need:
1) Simple bookkeeping services
2) Accounting advice that only someone with many years of senior financial experience as a CPA can provide.

The services are provided by two individuals. each of whom specialize in one of the areas.

We want the website to be clean without a lot of visual distraction but don't know how to make a boring subject interesting. We believe our potential clients, small business owners, need to find what they want quickly and easily without a lot of verbiage or distractions.

We've attached a draft of the homepage and have completed the text on most of the other pages.

Target Market(s)

small and early stage growth companies in San Diego North County

Industry/Entity Type

Accounting

Number of Pages Required

1 page

Font styles to use
Sans Serif

Colors
86cfc6
33b8a4
85cae6

Requirements
Must have
• We need a design for the website homepage that includes the name Daltonby as the logo. Must include a design for the name.
• Must have color in teal or greenish blue.
Nice to have
• White background, clean, clear, uncluttered.
• We would like to use the design in a Theme on a WordPress website. Themes Maple Harbor and Copper Lantern are appealing to us.
Should not have
• Moving pictures

```html
<!DOCTYPE html>
<html lang="en">
<head>
<meta charset="utf-8">
<title>Daltonby — Accounting and Bookkeeping</title>
<link href="https://fonts.googleapis.com/css2?family=Open+Sans:wght@400;600&family=Raleway:wght@400;500&display=swap" rel="stylesheet">
<style>
:root{
  --teal:#33b8a4;
  --teal-soft:#86cfc6;
  --sky:#85cae6;
  --ink:#333;
  --muted:#666;
  --light:#f4f4f4;
  --dark:#2b2b2b;
  --darker:#1f1f1f;
  --white:#fff;
}
*{margin:0;padding:0;box-sizing:border-box}
html,body{width:1200px;height:2913px;overflow:hidden}
body{position:relative;background:var(--white);font-family:"Open Sans",Arial,sans-serif;color:var(--ink)}
.abs{position:absolute}
.display{font-family:"Raleway",Arial,sans-serif;font-weight:400;text-transform:uppercase}

/* header */
.site-header{left:0;top:0;width:1200px;height:101px;border-top:5px solid var(--teal)}
.brand{left:97px;top:24px}
.brand-name{font-family:"Open Sans",Arial,sans-serif;font-weight:600;font-size:32px;color:var(--teal);letter-spacing:.5px;line-height:1}
.brand-tag{font-family:"Open Sans",Arial,sans-serif;font-size:10px;color:var(--teal);letter-spacing:1px;margin-top:5px}
.main-nav{right:92px;top:40px;display:flex;gap:59px;font-size:14px;color:var(--muted)}
.main-nav .active{color:var(--teal)}

/* hero */
.hero{left:0;top:101px;width:1200px;height:515px;background:linear-gradient(180deg,#7e9a5a 0%,#b7b670 35%,#a98a55 62%,#4d3a2a 100%)}
.hero-caption{left:503px;top:80px;width:612px;height:176px;background:rgba(51,184,164,.85);padding:20px 32px;color:var(--white)}
.hero-caption h1{font-family:"Raleway",Arial,sans-serif;font-weight:400;font-size:48px;letter-spacing:1px;line-height:1.1}
.hero-caption p{font-family:"Raleway",Arial,sans-serif;font-size:22px;line-height:1.35;margin-top:8px}
.hero-arrow{top:242px;width:34px;height:34px;border:2px solid rgba(255,255,255,.7);border-radius:50%}

/* welcome */
.section-title{width:1200px;text-align:center;font-size:28px;color:var(--ink);letter-spacing:2px}
.welcome-sub{top:708px;width:1200px;text-align:center;font-family:"Raleway",Arial,sans-serif;font-size:19px;letter-spacing:1px;text-transform:uppercase;color:var(--teal)}
.welcome-text{left:230px;top:745px;width:740px;text-align:center;font-size:11.5px;line-height:20px;color:var(--muted)}
.card{top:823px;width:307px}
.card-media{height:191px}
.card h3{font-size:16px;font-weight:600;text-align:center;margin-top:24px;color:var(--ink)}
.card h3.accent{color:var(--teal)}
.card p{font-size:11.5px;line-height:21px;text-align:center;color:var(--muted);margin-top:6px;padding:0 12px}
.card-rule{height:3px;background:var(--teal-soft);margin-top:30px}

/* services */
.services{left:0;top:1216px;width:1200px;height:396px;background:var(--light)}
.service{width:300px}
.service svg{position:absolute;left:0;top:0}
.service h4{margin-left:47px;font-size:18px;font-weight:400;color:var(--ink)}
.service p{margin-left:47px;font-size:11.5px;line-height:21px;color:var(--muted);text-align:justify;hyphens:auto;margin-top:4px;width:253px}

/* stats */
.stats{left:0;top:1616px;width:1200px;height:415px;background:linear-gradient(135deg,#3db9a7,#2a9e90 60%,#259387)}
.stats h2{top:54px;width:1200px;text-align:center;color:var(--white);font-size:30px;letter-spacing:2px}
.stats p{left:170px;top:104px;width:860px;text-align:center;color:var(--white);font-size:14px;line-height:27px}
.stat{top:195px;width:160px;height:160px;text-align:center;color:var(--white)}
.stat svg{position:absolute;left:0;top:0}
.stat strong{position:absolute;left:0;top:50px;width:160px;font-size:25px;font-weight:600}
.stat span{position:absolute;left:0;top:92px;width:160px;font-size:11px;text-transform:uppercase}

/* testimonials */
.quote-card{top:2183px;width:323px;height:128px;background:#f7f7f7;border:1px solid #eee;padding:38px 18px 0}
.quote-card p{font-size:11.5px;line-height:19px;color:#888}
.quote-badge{top:-30px;left:132px;width:60px;height:60px}
.person{top:2328px}
.avatar{position:absolute;left:0;top:0;width:60px;height:60px;border-radius:50%;border:3px solid var(--teal);background:#c8a58a}
.person b{position:absolute;left:80px;top:12px;font-weight:400;font-size:16px;white-space:nowrap}
.person small{position:absolute;left:80px;top:36px;font-size:12px;color:var(--muted);white-space:nowrap}

/* footer */
.site-footer{left:0;top:2453px;width:1200px;height:394px;background:var(--dark);color:var(--white)}
.site-footer h2{top:38px;width:1200px;text-align:center;font-size:22px;letter-spacing:2px}
.news-sub{top:72px;width:1200px;text-align:center;font-size:15px;color:#ddd}
.news-form{left:350px;top:122px;width:458px;height:43px;display:flex}
.news-input{flex:1;background:#444;color:#999;font-size:11px;padding:14px 20px}
.news-btn{width:70px;background:var(--teal);display:flex;align-items:center;justify-content:center}
.footer-col{top:226px}
.footer-col h5{font-family:"Raleway",Arial,sans-serif;font-weight:500;font-size:16px;letter-spacing:1px;margin-bottom:10px}
.footer-col li{list-style:none;font-size:11px;color:#bbb;line-height:24px;padding-left:3px}
.copyright{left:0;top:2847px;width:1200px;height:66px;background:var(--darker);color:#777;font-size:11px;text-align:center;line-height:66px}
.page-code{right:26px;top:2847px;line-height:66px;color:#ccc;font-size:13px}
</style>
</head>
<body>

<header class="site-header abs">
  <div class="brand abs">
    <div class="brand-name">Daltonby</div>
    <div class="brand-tag">ACCOUNTING AND BOOKKEEPING</div>
  </div>
  <nav class="main-nav abs">
    <span class="active">Home</span><span>About Us</span><span>Services</span><span>Experience</span><span>Resources</span><span>Contact Us</span>
  </nav>
</header>

<section class="hero abs" role="img" aria-label="Seedlings growing from stacks of coins in soil">
  <div class="hero-arrow abs" style="left:33px"><svg width="30" height="30" viewBox="0 0 30 30"><path d="M17 9l-6 6 6 6" fill="none" stroke="#fff" stroke-width="2"/></svg></div>
  <div class="hero-arrow abs" style="left:1133px"><svg width="30" height="30" viewBox="0 0 30 30"><path d="M13 9l6 6-6 6" fill="none" stroke="#fff" stroke-width="2"/></svg></div>
  <div class="hero-caption abs">
    <h1>DALTONBY</h1>
    <p>We simple book keeping services, financial<br>&amp; accounting advice for small start up companies.</p>
  </div>
</section>

<h2 class="section-title display abs" style="top:666px">Welcome To Daltonby</h2>
<div class="welcome-sub abs">We are Accounting and Bookkeeping</div>
<p class="welcome-text abs">Daltonby offers a flexible range of accounting and bookkeeping services and support for small and growing organizations in San Diego North County. We provide bookkeeping services specializing in LedgerBooks® at your offices or remotely from ours.</p>

<article class="card abs" style="left:99px">
  <div class="card-media" role="img" aria-label="Piggy bank on banknotes" style="background:linear-gradient(135deg,#e9e6e2,#d9b9bd 55%,#b9c2b0)"></div>
  <h3 class="accent">BOOK KEEPING SERVICES</h3>
  <p>It is a long established fact that a reader will be distracted by the readable content of a page when looking at its layout. The point of using Lorem</p>
  <div class="card-rule"></div>
</article>
<article class="card abs" style="left:447px">
  <div class="card-media" role="img" aria-label="Businessman touching floating currency symbols" style="background:linear-gradient(135deg,#2f4f7a,#6f95c4 55%,#b8cde6)"></div>
  <h3>FINANCIAL ADVICE</h3>
  <p>It is a long established fact that a reader will be distracted by the readable content of a page when looking at its layout. The point of using Lorem</p>
  <div class="card-rule"></div>
</article>
<article class="card abs" style="left:794px">
  <div class="card-media" role="img" aria-label="Colleagues meeting around a laptop" style="background:linear-gradient(135deg,#cfd3d6,#8a7a6c 55%,#3c3632)"></div>
  <h3>ACCOUNTING ADVICE</h3>
  <p>It is a long established fact that a reader will be distracted by the readable content of a page when looking at its layout. The point of using Lorem</p>
  <div class="card-rule"></div>
</article>

<section class="services abs">
  <h2 class="section-title display abs" style="top:52px">Our Services</h2>

  <div class="service abs" style="left:99px;top:122px">
    <svg width="28" height="28" viewBox="0 0 28 28"><rect x="3" y="6" width="22" height="18" rx="5" fill="#333"/><circle cx="10" cy="14" r="2" fill="#fff"/><circle cx="18" cy="14" r="2" fill="#fff"/></svg>
    <h4>Our Story</h4><p>Corvane is a California-based company focused on providing managed and optimized hosting services to small, medium-size ...</p>
  </div>
  <div class="service abs" style="left:447px;top:122px">
    <svg width="28" height="28" viewBox="0 0 28 28"><path d="M14 3L3 10h22z" fill="#333"/><rect x="5" y="12" width="18" height="11" fill="none" stroke="#333" stroke-width="2.5"/><rect x="3" y="23" width="22" height="3" fill="#333"/></svg>
    <h4>Our Story</h4><p>Corvane is a California-based company focused on providing managed and optimized hosting services to small, medium-size ...</p>
  </div>
  <div class="service abs" style="left:795px;top:122px">
    <svg width="28" height="28" viewBox="0 0 28 28"><circle cx="14" cy="16" r="10" fill="none" stroke="#333" stroke-width="2.5"/><path d="M14 16V10M12 3h4" stroke="#333" stroke-width="2.5"/></svg>
    <h4>Our Story</h4><p>Corvane is a California-based company focused on providing managed and optimized hosting services to small, medium-size ...</p>
  </div>
  <div class="service abs" style="left:99px;top:252px">
    <svg width="28" height="28" viewBox="0 0 28 28"><ellipse cx="12" cy="12" rx="9" ry="7" fill="none" stroke="#333" stroke-width="2"/><path d="M7 17l-3 5 6-3" fill="none" stroke="#333" stroke-width="2"/><ellipse cx="19" cy="19" rx="6" ry="5" fill="none" stroke="#333" stroke-width="2"/></svg>
    <h4>Data Center</h4><p>Corvane is a California-based company focused on providing managed and optimized hosting services to small, medium-size ...</p>
  </div>
  <div class="service abs" style="left:447px;top:252px">
    <svg width="28" height="28" viewBox="0 0 28 28"><ellipse cx="18" cy="20" rx="7" ry="3" fill="none" stroke="#333" stroke-width="2"/><ellipse cx="18" cy="15" rx="7" ry="3" fill="none" stroke="#333" stroke-width="2"/><circle cx="8" cy="9" r="5" fill="none" stroke="#333" stroke-width="2"/></svg>
    <h4>Data Center</h4><p>Corvane is a California-based company focused on providing managed and optimized hosting services to small, medium-size ...</p>
  </div>
  <div class="service abs" style="left:795px;top:252px">
    <svg width="28" height="28" viewBox="0 0 28 28"><path d="M3 25h23" stroke="#333" stroke-width="2"/><rect x="5" y="10" width="3" height="14" fill="#333"/><rect x="11" y="14" width="3" height="10" fill="#333"/><rect x="17" y="12" width="3" height="12" fill="#333"/><rect x="23" y="17" width="3" height="7" fill="#333"/><path d="M4 8l8 4 6-3 8 6" fill="none" stroke="#333" stroke-width="2"/></svg>
    <h4>Data Center</h4><p>Corvane is a California-based company focused on providing managed and optimized hosting services to small, medium-size ...</p>
  </div>
</section>

<section class="stats abs">
  <h2 class="display abs">We help you in book keeping &amp; accounting</h2>
  <p class="abs">There are many variations of passages of Lorem Ipsum available, but the majority have suffered alteration in some form, by injected humour, or randomised words which don't look even slightly believable. If you are going to use a passage</p>
  <div class="stat abs" style="left:167px">
    <svg width="160" height="160"><circle cx="80" cy="80" r="76" fill="none" stroke="rgba(255,255,255,.45)" stroke-width="4"/><circle cx="80" cy="80" r="76" fill="none" stroke="#85cae6" stroke-width="4" stroke-dasharray="120 400" transform="rotate(-90 80 80)"/></svg>
    <strong>248</strong><span>Year of Experience</span>
  </div>
  <div class="stat abs" style="left:404px">
    <svg width="160" height="160"><circle cx="80" cy="80" r="76" fill="none" stroke="rgba(255,255,255,.45)" stroke-width="4"/><circle cx="80" cy="80" r="76" fill="none" stroke="#85cae6" stroke-width="4" stroke-dasharray="110 400" transform="rotate(-90 80 80)"/></svg>
    <strong>1950</strong><span>Happy Customers</span>
  </div>
  <div class="stat abs" style="left:644px">
    <svg width="160" height="160"><circle cx="80" cy="80" r="76" fill="none" stroke="rgba(255,255,255,.45)" stroke-width="4"/><circle cx="80" cy="80" r="76" fill="none" stroke="#85cae6" stroke-width="4" stroke-dasharray="140 400" transform="rotate(-90 80 80)"/></svg>
    <strong>2686</strong><span>Satisfaction</span>
  </div>
  <div class="stat abs" style="left:883px">
    <svg width="160" height="160"><circle cx="80" cy="80" r="76" fill="none" stroke="rgba(255,255,255,.45)" stroke-width="4"/><circle cx="80" cy="80" r="76" fill="none" stroke="#85cae6" stroke-width="4" stroke-dasharray="180 400" transform="rotate(-90 80 80)"/></svg>
    <strong>3698</strong><span>Projects</span>
  </div>
</section>

<h2 class="section-title display abs" style="top:2081px">Our Testimonial</h2>

<div class="quote-card abs" style="left:99px">
  <svg class="quote-badge abs" viewBox="0 0 60 60"><circle cx="30" cy="30" r="29" fill="#86cfc6"/><circle cx="30" cy="30" r="23" fill="#33b8a4"/><path d="M21 26h7v7l-3 5h-3l2-5h-3zM32 26h7v7l-3 5h-3l2-5h-3z" fill="#fff"/></svg>
  <p>" Venture partners may earn the right to be a Partner according to the time period they spent and the evaluation process. Venture partners may earn the right to be a Partner according to the time "</p>
</div>
<div class="quote-card abs" style="left:439px">
  <svg class="quote-badge abs" viewBox="0 0 60 60"><circle cx="30" cy="30" r="29" fill="#86cfc6"/><circle cx="30" cy="30" r="23" fill="#33b8a4"/><path d="M21 26h7v7l-3 5h-3l2-5h-3zM32 26h7v7l-3 5h-3l2-5h-3z" fill="#fff"/></svg>
  <p>" Venture partners may earn the right to be a Partner according to the time period they spent and the evaluation process. Venture partners may earn the right to be a Partner according to the time "</p>
</div>
<div class="quote-card abs" style="left:779px">
  <svg class="quote-badge abs" viewBox="0 0 60 60"><circle cx="30" cy="30" r="29" fill="#86cfc6"/><circle cx="30" cy="30" r="23" fill="#33b8a4"/><path d="M21 26h7v7l-3 5h-3l2-5h-3zM32 26h7v7l-3 5h-3l2-5h-3z" fill="#fff"/></svg>
  <p>" Venture partners may earn the right to be a Partner according to the time period they spent and the evaluation process. Venture partners may earn the right to be a Partner according to the time "</p>
</div>

<div class="person abs" style="left:100px"><div class="avatar" role="img" aria-label="Client portrait"></div><b>Selim Aydar</b><small>Startup Harbor</small></div>
<div class="person abs" style="left:441px"><div class="avatar" role="img" aria-label="Client portrait"></div><b>Selim Aydar</b><small>Startup Harbor</small></div>
<div class="person abs" style="left:781px"><div class="avatar" role="img" aria-label="Client portrait"></div><b>Selim Aydar</b><small>Startup Harbor</small></div>

<footer class="site-footer abs">
  <h2 class="display abs">Newsletter</h2>
  <div class="news-sub abs">We promise only send the good things</div>
  <div class="news-form abs">
    <div class="news-input">Enter Your Mail Id</div>
    <div class="news-btn"><svg width="18" height="18" viewBox="0 0 18 18"><path d="M16 2L2 8l6 2 2 6z" fill="#fff"/></svg></div>
  </div>
  <div class="footer-col abs" style="left:97px"><h5>ABOUT US</h5><ul><li>Home</li><li>Service</li><li>Compare</li><li>Experience</li></ul></div>
  <div class="footer-col abs" style="left:315px"><h5>INFORMATION</h5><ul><li>Testimonials</li><li>Resources</li><li>Contact Us</li></ul></div>
  <div class="footer-col abs" style="left:538px"><h5>CUSTOMER</h5><ul><li>Privacy policy</li><li>Terms &amp; Conditions</li><li>Sitemap</li></ul></div>
  <div class="footer-col abs" style="left:763px"><h5>MAIN MENU</h5><ul><li>About Us</li><li>Services</li><li>Experience</li><li>Contact Us</li></ul></div>
  <div class="footer-col abs" style="left:988px"><h5>OUR PROJECTS</h5><ul><li>Neque porro</li><li>Quisquam lat</li><li>Quia dolor sit amet</li><li>The standard Lorem</li></ul></div>
</footer>
<div class="copyright abs">Copyright@2016 Company Name , All rights Reserved</div>
<div class="page-code abs">C15</div>

</body>
</html>
```